Brackenridge Strength Studio Chronic Pain Flyer

Double sided DL flyer required to promote a strength training studio to sufferers of chronic pain. Flyer will be displayed in osteopathy, chiropractic and massage clinics. Flyer should be clean, professional and appeal to an older (40+) demographic.

Target Market(s)

Chronic pain sufferers. Age 40+

Industry/Entity Type

Health And Wellness

Colors

Designer to choose colors to be used in the design.

Requirements
Must have
• See attached files for text copy and logo. Image(s) of people strength training with a coach or personal trainer, as well as images depicting pain in common parts of the body (such as those pictured in the supplied mock up)
• website address: brackenridgestrengthstudio.example.com.au
• phone number : 0452 918 304
• Street address: 4/63 Juniper Hollow Rd, Brackenridge
Nice to have
• Images such as in the attached files.

```html
<!DOCTYPE html>
<html lang="en">
<head>
<meta charset="utf-8">
<title>Brackenridge Strength Studio – Chronic Pain Flyer</title>
<link href="https://fonts.googleapis.com/css2?family=Oswald:wght@400;500;600&family=Open+Sans:ital,wght@0,400;0,600;0,700;1,600;1,700&family=Roboto+Condensed:wght@400;500&display=swap" rel="stylesheet">
<style>
  :root{
    --red:#c4161c;
    --red-deep:#9e1b1f;
    --charcoal:#333436;
    --ink:#2a2a2a;
    --grey-text:#3c3c3c;
    --paper:#ffffff;
    --canvas:#e6e6e6;
  }
  *{margin:0;padding:0;box-sizing:border-box}
  html,body{width:1095px;height:1200px;overflow:hidden;background:var(--canvas)}
  .canvas{position:relative;width:1095px;height:1200px}
  .flyer{position:absolute;top:140px;width:460px;height:920px;background:var(--paper);overflow:hidden;box-shadow:0 6px 18px rgba(0,0,0,.18)}
  .flyer--front{left:50px}
  .flyer--back{left:585px}

  /* front */
  .front-art{position:absolute;left:0;top:0;width:460px;height:470px}
  .brand{font-family:"Oswald",sans-serif;font-weight:500;color:var(--charcoal);text-transform:uppercase;letter-spacing:1px;display:flex;align-items:center;gap:8px}
  .brand__dot{width:12px;height:12px;border-radius:50%;background:var(--red);flex:none}
  .brand--front{position:absolute;left:44px;top:182px;font-size:18px;line-height:1.15;width:200px}
  .front-copy{position:absolute;left:0;top:470px;width:460px;height:379px;background:var(--charcoal);color:#fff}
  .headline{font-family:"Oswald",sans-serif;font-weight:600;text-align:center;text-transform:uppercase}
  .headline__top{position:absolute;top:26px;left:0;width:100%;font-size:40px;line-height:1}
  .headline__main{position:absolute;top:74px;left:0;width:100%;font-size:60px;line-height:1;display:flex;justify-content:center;align-items:center;gap:14px}
  .dots{display:flex;gap:6px}
  .dots span{width:20px;height:20px;border-radius:50%;background:var(--red)}
  .dots span:first-child{opacity:.7}
  .dots--right span:first-child{opacity:1}
  .dots--right span:last-child{opacity:.7}
  .subhead{position:absolute;top:148px;left:0;width:100%;text-align:center;font-family:"Oswald",sans-serif;font-weight:400;font-size:22px;line-height:1.2;color:var(--red);text-transform:uppercase}
  .front-body{position:absolute;left:18px;right:18px;top:190px;font-family:"Open Sans",sans-serif;font-size:15px;line-height:1.38;text-align:justify}
  .front-body p+p{margin-top:20px}
  .cta{position:absolute;left:18px;top:346px;font-family:"Oswald",sans-serif;font-style:italic;font-weight:500;font-size:14px;text-transform:uppercase;letter-spacing:-.2px}

  /* footer */
  .contact-bar{position:absolute;left:0;bottom:0;width:460px;height:71px;background:var(--paper);border-top:4px solid var(--red-deep);border-bottom:4px solid var(--red-deep);display:flex;align-items:center}
  .contact-phone{display:flex;align-items:center;gap:6px;padding-left:6px;width:226px;flex:none;border-right:2px solid var(--red-deep);height:44px}
  .contact-phone__num{font-family:"Oswald",sans-serif;font-weight:600;font-size:36px;color:var(--red);letter-spacing:-.5px;line-height:1}
  .contact-lines{padding-left:6px;padding-right:6px;min-width:0;font-family:"Roboto Condensed",sans-serif;font-size:10.5px;color:var(--red);display:flex;flex-direction:column;gap:5px}
  .contact-lines div{display:flex;align-items:center;gap:4px;white-space:nowrap}
  .icon{flex:none}

  /* back */
  .top-band{position:absolute;left:0;top:0;width:460px;height:22px;background:var(--charcoal)}
  .brand--back{position:absolute;left:0;top:78px;width:100%;justify-content:center;font-size:26px}
  .why{position:absolute;left:0;top:145px;width:100%;text-align:center;font-family:"Open Sans",sans-serif;font-weight:700;font-size:19px;color:var(--red);text-transform:uppercase}
  .back-body{position:absolute;left:27px;right:27px;top:178px;font-family:"Open Sans",sans-serif;font-size:12.6px;line-height:1.42;color:var(--grey-text);text-align:justify}
  .back-body p+p{margin-top:16px}
  .blog{display:block;text-align:center;font-style:italic;font-weight:700;color:var(--red)}
  .blog-url{display:block;text-align:center;font-style:italic;font-weight:600;color:var(--ink)}
  .services-band{position:absolute;left:0;top:393px;width:460px;height:37px}
  .services-band__title{position:absolute;left:0;top:0;width:100%;height:37px;line-height:37px;text-align:center;font-family:"Open Sans",sans-serif;font-weight:700;font-size:19px;color:#fff;text-transform:uppercase}
  .services{position:absolute;left:30px;top:442px;list-style:none}
  .services li{display:flex;align-items:center;gap:20px;height:50px;font-family:"Roboto Condensed",sans-serif;font-weight:500;font-size:21px;color:var(--ink);text-transform:uppercase}
  .services__icon{width:44px;height:44px;flex:none}
  .pain-band{position:absolute;left:0;top:685px;width:460px;height:54px}
  .pain-band__text{position:absolute;right:14px;top:32px;font-family:"Roboto Condensed",sans-serif;font-weight:500;font-size:15px;color:#fff;text-transform:uppercase}
  .pain-photos{position:absolute;left:0;top:739px;width:460px;height:110px}
</style>
</head>
<body>
<div class="canvas">

  <section class="flyer flyer--front" aria-label="Flyer front">
    <svg class="front-art" viewBox="0 0 460 470" width="460" height="470">
      <defs>
        <radialGradient id="figure-tone" cx="55%" cy="40%" r="70%">
          <stop offset="0" stop-color="#9a9a9a"/>
          <stop offset=".6" stop-color="#c9c9c9"/>
          <stop offset="1" stop-color="#e4e4e4"/>
        </radialGradient>
      </defs>
      <rect x="0" y="0" width="460" height="470" fill="var(--red-deep)"/>
      <rect role="img" aria-label="Greyscale photo of a seated person hugging their knees, with red markers on the neck, shoulder, back, elbow, wrist and knee showing common pain points" x="34" y="0" width="392" height="470" fill="url(#figure-tone)"/>
      <path d="M0 450 L0 515 L34 515 L34 442 L70 436 L92 444 L130 432 L170 440 L205 428 L240 438 L282 430 L320 442 L362 433 L400 438 L426 431 L426 515 L460 515 L460 450 L426 450 L426 470 L0 470 Z" fill="#fff"/>
      <path d="M0 470 L34 466 L60 460 L95 466 L130 455 L168 462 L205 450 L245 460 L285 452 L325 463 L365 454 L405 460 L440 452 L460 456 L460 470 Z" fill="var(--charcoal)"/>
    </svg>
    <div class="brand brand--front"><span class="brand__dot"></span>Brackenridge Strength Studio</div>

    <div class="front-copy">
      <h1 class="headline">
        <span class="headline__top">Health Through</span>
        <span class="headline__main"><span class="dots"><span></span><span></span></span>Strength<span class="dots dots--right"><span></span><span></span></span></span>
      </h1>
      <p class="subhead">You don’t have to live in pain</p>
      <div class="front-body">
        <p>Strength training has been shown to improve many chronic pain conditions and is now being routinely recommended by medical and health professionals</p>
        <p>Our private studio provides high quality strength training by expert strength coaches. We’ve helped countless people improve or eliminate chronic pain.</p>
      </div>
      <p class="cta">Contact us today and find out how we can help you.</p>
    </div>

    <footer class="contact-bar">
      <div class="contact-phone">
        <svg class="icon" width="16" height="16" viewBox="0 0 16 16"><rect width="16" height="16" rx="3" fill="var(--charcoal)"/><path d="M5 3.5l2 2-1 1.3c.6 1.3 1.6 2.3 2.9 2.9l1.3-1 2 2-1.2 1.5C7.8 12 4 8.2 3.8 4.7Z" fill="#fff"/></svg>
        <span class="contact-phone__num">0452 918 304</span>
      </div>
      <div class="contact-lines">
        <div><svg class="icon" width="12" height="12" viewBox="0 0 12 12"><rect width="12" height="12" rx="2" fill="var(--charcoal)"/><circle cx="6" cy="6" r="3.5" fill="none" stroke="#fff" stroke-width="1.2"/></svg>brackenridgestrengthstudio.example.com.au</div>
        <div><svg class="icon" width="12" height="12" viewBox="0 0 12 12"><rect width="12" height="12" rx="2" fill="var(--charcoal)"/><path d="M6 2a2.6 2.6 0 0 1 2.6 2.6C8.6 6.6 6 10 6 10S3.4 6.6 3.4 4.6A2.6 2.6 0 0 1 6 2Z" fill="#fff"/></svg>4/63 Juniper Hollow Rd, Brackenridge</div>
      </div>
    </footer>
  </section>

  <section class="flyer flyer--back" aria-label="Flyer back">
    <div class="top-band"></div>
    <div class="brand brand--back"><span class="brand__dot"></span>Brackenridge Strength Studio</div>
    <h2 class="why">Why Brackenridge Strength Studio?</h2>
    <div class="back-body">
      <p>BSS is a boutique personal training and group fitness facility providing an exceptional level of service to our dedicated clients. BSS is NOT a gym but a private training studio, committed to providing a welcoming and non-judgmental place to train for people looking to get real results. If you dislike the gym but need to exercise, our studio setting is just the place for you!</p>
      <p>Our philosophy is "Health Through Strength" and we believe that's exactly what we're achieving. You can read more about our
        <span class="blog">"No Brain No Gain" approach to health and fitness through our blog</span>
        <span class="blog-url">www.strongandsteadyblog.example.com</span></p>
    </div>

    <div class="services-band">
      <svg width="460" height="37" viewBox="0 0 460 37">
        <rect x="0" y="0" width="55" height="37" fill="var(--red)"/>
        <rect x="62" y="0" width="16" height="37" fill="var(--red)"/>
        <rect x="84" y="0" width="16" height="37" fill="var(--red)"/>
        <rect x="108" y="0" width="244" height="37" fill="var(--red)"/>
        <rect x="360" y="0" width="16" height="37" fill="var(--red)"/>
        <rect x="382" y="0" width="16" height="37" fill="var(--red)"/>
        <rect x="405" y="0" width="55" height="37" fill="var(--red)"/>
      </svg>
      <div class="services-band__title">Our Services</div>
    </div>

    <ul class="services">
      <li><svg class="services__icon" viewBox="0 0 44 44" aria-hidden="true"><rect width="44" height="44" rx="6" fill="var(--red)"/><g transform="rotate(-40 22 22)" fill="#fff"><rect x="9" y="15" width="5" height="14" rx="1"/><rect x="14" y="17" width="3" height="10" rx="1"/><rect x="17" y="20.5" width="10" height="3"/><rect x="27" y="17" width="3" height="10" rx="1"/><rect x="30" y="15" width="5" height="14" rx="1"/></g></svg>Personal Training</li>
      <li><svg class="services__icon" viewBox="0 0 44 44" aria-hidden="true"><rect width="44" height="44" rx="6" fill="var(--red)"/><path d="M22 8l11 4v8c0 8-5 13-11 16-6-3-11-8-11-16v-8Z" fill="#fff"/><path d="M22 13l6 2.2v5c0 5-3 8-6 10Z" fill="var(--red)"/></svg>Self Defence</li>
      <li><svg class="services__icon" viewBox="0 0 44 44" aria-hidden="true"><rect width="44" height="44" rx="6" fill="var(--red)"/><path d="M18 9h8v9h9v8h-9v9h-8v-9H9v-8h9Z" fill="#fff"/></svg>Rehab/Exercise Physiology</li>
      <li><svg class="services__icon" viewBox="0 0 44 44" aria-hidden="true"><rect width="44" height="44" rx="6" fill="var(--red)"/><rect x="9" y="11" width="26" height="23" rx="4" fill="#fff"/><path d="M15 21a7 7 0 0 1 14 0Z" fill="var(--red)"/><path d="M22 21l3-5" stroke="#fff" stroke-width="1.6"/></svg>Body Composition</li>
      <li><svg class="services__icon" viewBox="0 0 44 44" aria-hidden="true"><rect width="44" height="44" rx="6" fill="var(--red)"/><rect x="8" y="27" width="28" height="5" rx="1.5" fill="#fff"/><rect x="10" y="32" width="3" height="5" fill="#fff"/><rect x="31" y="32" width="3" height="5" fill="#fff"/><path d="M12 25c3-5 10-7 20-5v3H12Z" fill="#fff"/></svg>Massage</li>
    </ul>

    <div class="pain-band">
      <svg width="460" height="54" viewBox="0 0 460 54"><path d="M0 54 L0 40 L460 0 L460 54 Z" fill="var(--charcoal)"/></svg>
      <span class="pain-band__text">You don’t have to live in pain</span>
    </div>
    <svg class="pain-photos" viewBox="0 0 460 110" width="460" height="110">
      <defs>
        <radialGradient id="pain-a" cx="50%" cy="70%" r="60%"><stop offset="0" stop-color="#e2474c"/><stop offset=".45" stop-color="#d9b2ac"/><stop offset="1" stop-color="#efefef"/></radialGradient>
        <radialGradient id="pain-b" cx="50%" cy="35%" r="60%"><stop offset="0" stop-color="#e2474c"/><stop offset=".45" stop-color="#c9bcb8"/><stop offset="1" stop-color="#eeeeee"/></radialGradient>
        <radialGradient id="pain-c" cx="55%" cy="40%" r="60%"><stop offset="0" stop-color="#e2474c"/><stop offset=".45" stop-color="#c4bab7"/><stop offset="1" stop-color="#eaeaea"/></radialGradient>
      </defs>
      <rect role="img" aria-label="Photo of a bare back with lower back pain highlighted in red" x="0" y="0" width="153" height="110" fill="url(#pain-a)"/>
      <rect role="img" aria-label="Photo of a shoulder held in pain, highlighted in red" x="153" y="0" width="154" height="110" fill="url(#pain-b)"/>
      <rect role="img" aria-label="Photo of hands holding a painful knee, highlighted in red" x="307" y="0" width="153" height="110" fill="url(#pain-c)"/>
    </svg>

    <footer class="contact-bar">
      <div class="contact-phone">
        <svg class="icon" width="16" height="16" viewBox="0 0 16 16"><rect width="16" height="16" rx="3" fill="var(--charcoal)"/><path d="M5 3.5l2 2-1 1.3c.6 1.3 1.6 2.3 2.9 2.9l1.3-1 2 2-1.2 1.5C7.8 12 4 8.2 3.8 4.7Z" fill="#fff"/></svg>
        <span class="contact-phone__num">0452 918 304</span>
      </div>
      <div class="contact-lines">
        <div><svg class="icon" width="12" height="12" viewBox="0 0 12 12"><rect width="12" height="12" rx="2" fill="var(--charcoal)"/><circle cx="6" cy="6" r="3.5" fill="none" stroke="#fff" stroke-width="1.2"/></svg>brackenridgestrengthstudio.example.com.au</div>
        <div><svg class="icon" width="12" height="12" viewBox="0 0 12 12"><rect width="12" height="12" rx="2" fill="var(--charcoal)"/><path d="M6 2a2.6 2.6 0 0 1 2.6 2.6C8.6 6.6 6 10 6 10S3.4 6.6 3.4 4.6A2.6 2.6 0 0 1 6 2Z" fill="#fff"/></svg>4/63 Juniper Hollow Rd, Brackenridge</div>
      </div>
    </footer>
  </section>

</div>
</body>
</html>
```